Business Card Design

we are a brand new cable TV network devoted to self improvement and leading a better life called FLOURIVO TV.I have a logo. We have 3 executives that need cards.I want it to be a heavy stock card: professional but showing our creative nature

Industry/Entity Type

Business

Contact Information for Business Card

CLAUDIA SAENZ AMLIECEO350 San Juan DrPonte Vedra Beach FL 32082904-473-5953

```html
<!DOCTYPE html>
<html lang="en">
<head>
<meta charset="utf-8">
<title>Flourivo TV – Business Card</title>
<link rel="stylesheet" href="https://fonts.googleapis.com/css2?family=Open+Sans:wght@400;600;700;800&display=swap">
<style>
  :root {
    --stage: #141414;
    --paper: #ffffff;
    --brand-red: #b0222a;
    --name-red: #cc1d24;
    --ink-dark: #231f20;
    --ink-grey: #5a5a5a;
    --back-top: #e3a596;
    --back-mid: #8e2a2d;
    --back-bottom: #d81f27;
  }
  * { margin: 0; padding: 0; box-sizing: border-box; }
  html, body {
    width: 1200px;
    height: 900px;
    overflow: hidden;
    background: var(--stage);
    font-family: "Open Sans", Arial, sans-serif;
  }
  .stage {
    position: relative;
    width: 1200px;
    height: 900px;
  }
  .card {
    position: absolute;
    top: 170px;
    width: 347px;
    height: 561px;
  }
  .card--front {
    left: 259px;
    background: var(--paper);
    text-align: center;
  }
  .card--back {
    left: 631px;
    background: linear-gradient(to bottom,
      var(--back-top) 0%,
      #b06560 30%,
      var(--back-mid) 55%,
      #b42229 78%,
      var(--back-bottom) 100%);
  }
  .tab {
    position: absolute;
    left: 102px;
    width: 143px;
    height: 30px;
    background: var(--brand-red);
  }
  .tab--top { top: 0; }
  .tab--bottom { bottom: 0; height: 28px; }
  .brand-name {
    position: absolute;
    top: 175px;
    left: 0;
    width: 100%;
    font-weight: 800;
    font-size: 38px;
    letter-spacing: -0.5px;
    color: var(--ink-dark);
  }
  .person {
    position: absolute;
    top: 258px;
    left: 0;
    width: 100%;
  }
  .person__name {
    font-weight: 600;
    font-size: 18.5px;
    line-height: 22px;
    color: var(--name-red);
  }
  .person__role {
    font-size: 14.5px;
    line-height: 18px;
    color: var(--ink-grey);
  }
  .address {
    position: absolute;
    top: 314px;
    left: 0;
    width: 100%;
    font-style: normal;
    font-size: 15px;
    line-height: 20px;
    color: var(--ink-grey);
  }
  .phone {
    position: absolute;
    top: 367px;
    left: 0;
    width: 100%;
    font-size: 15px;
    line-height: 20px;
    color: var(--ink-grey);
    display: flex;
    justify-content: center;
    align-items: center;
    gap: 8px;
  }
  .phone__icon { width: 12px; height: 12px; fill: var(--name-red); }
</style>
</head>
<body>
  <main class="stage">
    <section class="card card--front" aria-label="Card front">
      <div class="tab tab--top"></div>
      <h1 class="brand-name">FLOURIVO TV</h1>
      <div class="person">
        <p class="person__name">MIRELLA OKAFOR DUNST</p>
        <p class="person__role">CEO</p>
      </div>
      <address class="address">
        718 Harlow Creek Dr<br>
        Cedarholt Springs NV 89417
      </address>
      <p class="phone">
        <svg class="phone__icon" viewBox="0 0 24 24" aria-hidden="true">
          <path d="M6.6 10.8a15.1 15.1 0 0 0 6.6 6.6l2.2-2.2a1 1 0 0 1 1-.25 11.4 11.4 0 0 0 3.6.57 1 1 0 0 1 1 1V20a1 1 0 0 1-1 1A17 17 0 0 1 3 4a1 1 0 0 1 1-1h3.5a1 1 0 0 1 1 1 11.4 11.4 0 0 0 .57 3.6 1 1 0 0 1-.25 1z"/>
        </svg>
        <span>555-618-2047</span>
      </p>
      <div class="tab tab--bottom"></div>
    </section>
    <section class="card card--back" aria-label="Card back"></section>
  </main>
</body>
</html>
```